Professional digital stationary

We need a digital stationary for our brand, we already have a logo and based on that we need a design for Word, Powerpoint, mailings and Linkedin. We need to be able to re use the stationary for other things like other social media. So basically what we ask is a template for Powerpoint and Word, some e-mail headers and a nice and professional Linkedin Header.

Target Market(s)

recruitment

Font styles to use
Sans Serif

```html
<!DOCTYPE html>
<html lang="en">
<head>
<meta charset="utf-8">
<title>Bright Path – Thank You</title>
<link rel="stylesheet" href="https://fonts.googleapis.com/css2?family=Montserrat:wght@700&family=Open+Sans:wght@300;400;600&display=swap">
<style>
  :root {
    --green: #9ccd6c;
    --ink: #4a4a4a;
    --ink-soft: #555555;
    --paper: #ffffff;
    --photo-light: #e9e4d6;
    --photo-mid: #b9b3a4;
    --photo-dark: #5d6470;
  }
  * { margin: 0; padding: 0; box-sizing: border-box; }
  html, body { width: 1200px; height: 675px; overflow: hidden; background: var(--paper); }
  .slide {
    position: relative;
    width: 1200px;
    height: 675px;
    overflow: hidden;
    background: var(--paper);
    font-family: "Open Sans", sans-serif;
    color: var(--ink-soft);
  }
  .slide__photo {
    position: absolute;
    inset: 0;
    background:
      radial-gradient(ellipse 520px 300px at 640px 40px, #fbf8ef 0%, rgba(251,248,239,0) 70%),
      linear-gradient(120deg, var(--photo-light) 0%, var(--photo-mid) 45%, var(--photo-dark) 75%, #8f97a2 100%);
  }
  .slide__shape {
    position: absolute;
    inset: 0;
    width: 1200px;
    height: 675px;
  }
  .brand {
    position: absolute;
    left: 82px;
    top: 160px;
  }
  .brand__name {
    font-family: "Open Sans", sans-serif;
    font-weight: 600;
    font-size: 44px;
    line-height: 1;
    color: var(--ink);
  }
  .brand__tagline {
    margin-top: 8px;
    font-family: "Open Sans", sans-serif;
    font-weight: 400;
    font-size: 12.5px;
    color: var(--ink-soft);
  }
  .closing {
    position: absolute;
    left: 80px;
    top: 352px;
  }
  .closing__title {
    font-family: "Montserrat", sans-serif;
    font-weight: 700;
    font-size: 70px;
    line-height: 1;
    color: var(--green);
  }
  .closing__subtitle {
    margin-top: 8px;
    margin-left: 2px;
    font-size: 31px;
    font-weight: 300;
    color: var(--ink-soft);
  }
  .contact {
    position: absolute;
    left: 83px;
    top: 547px;
    display: flex;
    gap: 52px;
    font-size: 19.5px;
    line-height: 26.5px;
    color: var(--ink-soft);
  }
  .contact__list { list-style: none; }
  .contact__item { display: flex; align-items: center; gap: 10px; }
  .contact__icon { width: 17px; height: 17px; fill: var(--green); flex: none; }
  .contact__address { font-style: normal; }
</style>
</head>
<body>
<main class="slide">
  <div class="slide__photo" role="img" aria-label="Photo of two business people in suits reviewing printed bar charts with a pen and calculator on an office desk"></div>

  <svg class="slide__shape" viewBox="0 0 1366 768" preserveAspectRatio="none" aria-hidden="true">
    <path fill="#ffffff" d="M0 0 H150 C200 60 300 95 420 100 C470 105 490 140 490 200 C490 270 520 310 600 320 C700 335 770 380 800 470 C830 570 880 680 1050 768 H0 Z"/>
  </svg>

  <header class="brand">
    <div class="brand__name">brightpath</div>
    <div class="brand__tagline">More growth, more freedom</div>
  </header>

  <section class="closing">
    <h1 class="closing__title">Thank You!</h1>
    <p class="closing__subtitle">Stay In Touch With Us...</p>
  </section>

  <footer class="contact">
    <ul class="contact__list">
      <li class="contact__item">
        <svg class="contact__icon" viewBox="0 0 24 24" aria-hidden="true"><path d="M6.6 10.8a15.1 15.1 0 0 0 6.6 6.6l2.2-2.2a1 1 0 0 1 1-.25 11.4 11.4 0 0 0 3.6.57 1 1 0 0 1 1 1V20a1 1 0 0 1-1 1A17 17 0 0 1 3 4a1 1 0 0 1 1-1h3.5a1 1 0 0 1 1 1c0 1.25.2 2.45.57 3.57a1 1 0 0 1-.25 1z"/></svg>
        <span>+31 30 41 86 219</span>
      </li>
      <li class="contact__item">
        <svg class="contact__icon" viewBox="0 0 24 24" aria-hidden="true"><path d="M2 5h20v14H2z"/><path d="M3 6l9 7 9-7" fill="none" stroke="#fff" stroke-width="1.6"/></svg>
        <span>info@brightpath.nl</span>
      </li>
      <li class="contact__item">
        <svg class="contact__icon" viewBox="0 0 24 24" aria-hidden="true"><circle cx="12" cy="12" r="10"/><path d="M2 12h20M12 2c3 3 3 17 0 20M12 2c-3 3-3 17 0 20M4 7h16M4 17h16" fill="none" stroke="#fff" stroke-width="1.3"/></svg>
        <span>www.brightpath.nl</span>
      </li>
    </ul>
    <address class="contact__address">
      Bright Path<br>
      Lindenlaan 12, 3581 GD<br>
      Utrecht
    </address>
  </footer>
</main>
</body>
</html>
```